Birch Flooring Supply

Basic one-sided business card design using the attached logo. Vintage americana theme. Font is modified Arial Nova Cond, but anything that coordinates can be used

```html
<!DOCTYPE html>
<html lang="en">
<head>
<meta charset="utf-8">
<title>Birch Flooring Supply – Business Card</title>
<link rel="stylesheet" href="https://fonts.googleapis.com/css2?family=Roboto:wght@400&family=Roboto+Condensed:wght@700&display=swap">
<style>
  :root {
    --page-bg: #d9d9db;
    --card-bg: #f7f7f7;
    --pattern-tone: #e6e6e6;
    --ink: #161616;
    --band: #121212;
    --gold: #b49a78;
    --text: #1c1c1c;
    --muted: #4a4a4a;
    --rule: #2a2a2a;
  }
  html, body {
    margin: 0;
    width: 1200px;
    height: 1200px;
    overflow: hidden;
    background: var(--page-bg);
  }
  .canvas {
    position: relative;
    width: 1200px;
    height: 1200px;
  }
  .card {
    position: absolute;
    left: 100px;
    top: 313px;
    width: 1000px;
    height: 574px;
    background: var(--card-bg);
    overflow: hidden;
    box-shadow: 0 14px 30px rgba(0,0,0,0.22);
  }
  .card__texture {
    position: absolute;
    inset: 0;
    background: linear-gradient(135deg, var(--card-bg) 0%, var(--pattern-tone) 50%, var(--card-bg) 100%);
  }
  .band {
    position: absolute;
    left: 0;
    right: 0;
    top: 144px;
    height: 98px;
    background: var(--band);
  }
  .band__stripe {
    position: absolute;
    left: 0;
    right: 0;
    height: 9px;
    background: var(--gold);
  }
  .band__stripe--top { top: 10px; }
  .band__stripe--bottom { bottom: 10px; }
  .brand {
    position: absolute;
    left: 50%;
    top: 144px;
    height: 98px;
    transform: translateX(-50%);
    display: flex;
    align-items: center;
    gap: 16px;
    padding: 0 28px;
    background: var(--band);
  }
  .brand__dot {
    width: 26px;
    height: 26px;
    border-radius: 50%;
    background: var(--gold);
    flex: none;
  }
  .brand__name {
    font-family: "Roboto Condensed", "Arial Narrow", sans-serif;
    font-weight: 700;
    font-size: 40px;
    letter-spacing: 1px;
    color: #ffffff;
    white-space: nowrap;
    text-transform: uppercase;
  }
  .contact-block {
    position: absolute;
    top: 372px;
    left: 0;
    right: 0;
    display: flex;
    justify-content: center;
    align-items: stretch;
    font-family: "Roboto", Arial, sans-serif;
  }
  .person {
    text-align: left;
    padding-right: 18px;
    padding-top: 12px;
  }
  .person__name {
    font-size: 40px;
    color: var(--text);
    line-height: 1.1;
  }
  .person__role {
    font-size: 22px;
    color: var(--muted);
    text-transform: uppercase;
    margin-top: 2px;
  }
  .divider {
    width: 2px;
    background: var(--rule);
    margin-right: 18px;
  }
  .details {
    list-style: none;
    margin: 0;
    padding: 0;
  }
  .details__item {
    display: flex;
    align-items: center;
    gap: 14px;
    font-size: 30px;
    color: var(--text);
    line-height: 39px;
  }
  .details__icon {
    width: 22px;
    height: 22px;
    flex: none;
  }
</style>
</head>
<body>
<main class="canvas">
  <section class="card" aria-label="Birch Flooring Supply business card">
    <div class="card__texture" role="img" aria-label="Light grey repeating diamond lattice background pattern"></div>

    <div class="band">
      <div class="band__stripe band__stripe--top"></div>
      <div class="band__stripe band__stripe--bottom"></div>
    </div>

    <div class="brand">
      <span class="brand__dot"></span>
      <span class="brand__name">Birch Flooring Supply</span>
    </div>

    <div class="contact-block">
      <div class="person">
        <div class="person__name">Dana Ellis</div>
        <div class="person__role">Director</div>
      </div>
      <div class="divider"></div>
      <ul class="details">
        <li class="details__item">
          <svg class="details__icon" viewBox="0 0 24 24" aria-hidden="true"><path fill="#1c1c1c" d="M6.6 10.8a15.1 15.1 0 0 0 6.6 6.6l2.2-2.2a1 1 0 0 1 1-.25 11.4 11.4 0 0 0 3.6.57 1 1 0 0 1 1 1V20a1 1 0 0 1-1 1A17 17 0 0 1 3 4a1 1 0 0 1 1-1h3.5a1 1 0 0 1 1 1c0 1.25.2 2.45.57 3.57a1 1 0 0 1-.25 1z"/></svg>
          5550142876
        </li>
        <li class="details__item">
          <svg class="details__icon" viewBox="0 0 24 24" aria-hidden="true"><rect x="2" y="5" width="20" height="14" fill="#1c1c1c"/><path d="M2.5 5.5 12 13l9.5-7.5" fill="none" stroke="#f7f7f7" stroke-width="1.6"/></svg>
          hello@birchflooring.com
        </li>
        <li class="details__item">
          <svg class="details__icon" viewBox="0 0 24 24" aria-hidden="true"><circle cx="12" cy="12" r="10" fill="#1c1c1c"/><g fill="none" stroke="#f7f7f7" stroke-width="1.3"><ellipse cx="12" cy="12" rx="4" ry="10"/><path d="M2 12h20M4 7h16M4 17h16"/></g></svg>
          www.birchflooring.com
        </li>
      </ul>
    </div>
  </section>
</main>
</body>
</html>
```